OLUM Sign
OLUM leasing sign
#12 I'd like to go with this design with a few minor changes. Could you please change the font of Daniel Pruett to something that works better with the other font Office space? and can you remove the rectangles under the phone number? I promise i'll respond more quickly once i see the revisions.
additional comment on 23 -24. I think I like these for their clean simplicity (although they need the required information and the proper logo)
#23 ,#24 These looks different - good. Can you try a grey background, with correct logo (maybe in white). There is now an .eps file available. The sign must have phone number, "Office Space", and Realtor's name. use only the colors in logo, and black.
Dear PH, thanks for your valuable feedback.Will submit some more design options...regards,
will upload vector file. these designs are not what we are looking for. we want an eye catching creative design that doesn't look like a typical leasing sign.
Dear PH, Can you please upload the vector file (.ai or .eps) of the logo.Regards.

```html
<!DOCTYPE html>
<html lang="en">
<head>
<meta charset="utf-8">
<title>OLUM Leasing Sign – Office Space Available</title>
<link rel="stylesheet" href="https://fonts.googleapis.com/css2?family=Arimo:wght@400;700&family=Russo+One&family=Nunito:wght@900&display=swap">
<style>
  :root {
    --sky-light: #fde9a8;
    --sky-mid: #f8b868;
    --sky-edge: #e07a2c;
    --wood-light: #a85f30;
    --wood-dark: #5e2c12;
    --post-tone: #7a4a22;
    --foliage-tone: #5a9430;
    --headline-red: #d8232a;
    --headline-edge: #5a0c0c;
    --phone-edge: #7a0e10;
    --ink: #111111;
    --white: #ffffff;
    --logo-card: #f1f1f1;
    --logo-ink: #3a3a3a;
  }
  html, body { margin: 0; padding: 0; overflow: hidden; }
  body { width: 1200px; height: 799px; background: #ffffff; }

  .sign {
    position: relative;
    width: 1200px;
    height: 799px;
    overflow: hidden;
    background: radial-gradient(ellipse 70% 75% at 50% 55%, var(--sky-light) 0%, var(--sky-mid) 60%, var(--sky-edge) 100%);
    font-family: "Arimo", Arial, sans-serif;
  }

  .post {
    position: absolute;
    top: 0;
    bottom: 0;
    background: var(--post-tone);
  }
  .post--left { left: 0; width: 96px; }
  .post--right { right: 0; width: 90px; }

  .banner {
    position: absolute;
    left: 0;
    top: 12px;
    width: 1200px;
    height: 228px;
    background: linear-gradient(180deg, var(--wood-light), var(--wood-dark));
  }
  .banner__label {
    position: absolute;
    left: 0;
    right: 0;
    top: 44px;
    margin: 0;
    text-align: center;
    font-family: "Arimo", Arial, sans-serif;
    font-weight: 400;
    font-size: 142px;
    line-height: 1;
    letter-spacing: 4px;
    color: var(--white);
    text-shadow: 0 3px 4px rgba(0,0,0,0.45);
  }

  .foliage {
    position: absolute;
    background: linear-gradient(180deg, var(--foliage-tone), #3f7420);
  }
  .foliage--left { left: 0; top: 614px; width: 180px; height: 185px; }
  .foliage--right { right: 0; top: 684px; width: 132px; height: 115px; }

  .headline {
    position: absolute;
    left: 0;
    right: 0;
    top: 306px;
    margin: 0;
    text-align: center;
    font-family: "Russo One", sans-serif;
    font-weight: 400;
    font-size: 108px;
    line-height: 1;
    letter-spacing: 4px;
    color: var(--headline-red);
    -webkit-text-stroke: 4px var(--headline-edge);
    paint-order: stroke fill;
    text-shadow: 0 4px 3px rgba(0,0,0,0.35);
  }

  .phone {
    position: absolute;
    left: 150px;
    top: 466px;
    display: flex;
    align-items: center;
    gap: 30px;
  }
  .phone__icon { width: 130px; height: 100px; }
  .phone__number {
    font-family: "Nunito", sans-serif;
    font-weight: 900;
    font-size: 100px;
    line-height: 1;
    color: var(--ink);
    letter-spacing: 1px;
  }

  .contact {
    position: absolute;
    left: 192px;
    top: 660px;
  }
  .contact__label {
    margin: 0 0 10px 0;
    font-size: 36px;
    line-height: 1;
    color: var(--ink);
  }
  .contact__name {
    margin: 0;
    font-family: "Russo One", sans-serif;
    font-size: 44px;
    line-height: 1;
    color: var(--headline-red);
    -webkit-text-stroke: 6px var(--white);
    paint-order: stroke fill;
    letter-spacing: 1px;
  }

  .brand-card {
    position: absolute;
    left: 600px;
    top: 643px;
    width: 492px;
    height: 180px;
    border-radius: 18px;
    background: linear-gradient(180deg, #ffffff, var(--logo-card));
    box-shadow: 0 0 0 3px rgba(120,120,120,0.35);
    display: flex;
    justify-content: center;
    padding-top: 24px;
    box-sizing: border-box;
  }
  .brand-card__name {
    font-family: "Russo One", sans-serif;
    font-size: 100px;
    line-height: 1;
    color: var(--logo-ink);
    letter-spacing: 6px;
  }
</style>
</head>
<body>
<main class="sign">
  <div class="post post--left" role="img" aria-label="Wooden tree-trunk post on the left edge"></div>
  <div class="post post--right" role="img" aria-label="Wooden tree-trunk post on the right edge"></div>

  <div class="banner" role="img" aria-label="Bolted wooden plank banner across the top">
    <p class="banner__label">AVAILABLE</p>
  </div>

  <h1 class="headline">OFFICE SPACE</h1>

  <div class="phone">
    <svg class="phone__icon" viewBox="0 0 140 106" aria-hidden="true">
      <path d="M8 34 Q70 -6 132 34 L124 50 L98 44 L96 32 Q70 24 44 32 L42 44 L16 50 Z" fill="var(--headline-red)" stroke="var(--phone-edge)" stroke-width="3"/>
      <path d="M40 50 L100 50 L126 100 L14 100 Z" fill="var(--headline-red)" stroke="var(--phone-edge)" stroke-width="3"/>
      <circle cx="70" cy="74" r="18" fill="#f4f4f4" stroke="var(--phone-edge)" stroke-width="3"/>
      <circle cx="70" cy="74" r="6" fill="var(--headline-red)"/>
    </svg>
    <span class="phone__number">215-555-0147</span>
  </div>

  <div class="foliage foliage--left" role="img" aria-label="Green leafy plant with a yellow flower"></div>
  <div class="foliage foliage--right" role="img" aria-label="Green leafy plant"></div>

  <div class="contact">
    <p class="contact__label">Contact Person</p>
    <p class="contact__name">DANIEL PRUETT</p>
  </div>

  <div class="brand-card">
    <span class="brand-card__name">OLUM</span>
  </div>
</main>
</body>
</html>
```